Gombrevo business card

Based on company logo and website given , to design a business card temple. Slogan "Your furry friends deserves the best"
Color style please refer to our website

```html
<!DOCTYPE html>
<html lang="en">
<head>
<meta charset="utf-8">
<title>Gombrevo Stationery</title>
<link href="https://fonts.googleapis.com/css2?family=Montserrat:wght@400;500;600;700&family=Tinos&display=swap" rel="stylesheet">
<style>
  :root{
    --olive:#bdb04a;
    --forest:#142a27;
    --paper:#ffffff;
    --backdrop:#d0d0d0;
    --ink:#1a1a1a;
    --muted:#6b6b6b;
  }
  *{box-sizing:border-box;margin:0;padding:0}
  html,body{width:1200px;height:900px;overflow:hidden}
  body{background:var(--backdrop);position:relative;font-family:"Montserrat",sans-serif}

  .sheet{position:absolute;background:var(--paper);overflow:hidden}

  /* Letterhead */
  .letterhead{left:61px;top:115px;width:492px;height:697px}
  .letterhead__logo-box{position:absolute;left:48px;top:0;width:74px;height:89px;background:var(--forest);display:flex;align-items:center;justify-content:center}
  .wordmark{font-family:"Montserrat",sans-serif;font-weight:600;letter-spacing:-0.02em;white-space:nowrap;line-height:1}
  .letterhead__logo-box .wordmark{color:var(--olive);font-size:13px;margin-top:14px}
  .letterhead__company{position:absolute;right:48px;top:49px;color:var(--olive);font-weight:700;font-size:18px;white-space:nowrap}
  .letterhead__rule{position:absolute;left:48px;width:396px;height:1px;background:var(--olive);opacity:.7}
  .letterhead__rule--top{top:93px}
  .letterhead__rule--bottom{top:641px}
  .letter{position:absolute;left:48px;top:153px;width:396px;font-family:"Tinos",serif;font-size:9.8px;line-height:12px;color:var(--ink)}
  .letter__greeting{margin-bottom:12px}
  .letter p.letter__para{text-align:justify;text-indent:30px;margin-bottom:12px}
  .letter__signature{position:absolute;left:48px;top:498px;width:80px;height:34px;background:linear-gradient(90deg,#f2f2f2,#e6e6e6)}
  .letter__closing{position:absolute;left:48px;top:547px;font-family:"Tinos",serif;font-size:9.8px;line-height:12px;color:var(--ink)}
  .letterhead__footer{position:absolute;left:48px;top:651px;width:396px;height:20px}
  .letterhead__footer .contact{position:absolute;top:0;display:flex;align-items:center;gap:6px;height:20px;font-size:6.6px;line-height:8px;color:var(--olive)}
  .letterhead__footer .contact svg{width:8px;height:8px}
  .contact--phone{left:0}
  .contact--web{left:138px}
  .contact--address{right:0}
  .letterhead__bar{position:absolute;top:687px;height:10px}
  .letterhead__bar--olive{left:0;width:442px;background:var(--olive)}
  .letterhead__bar--forest{left:446px;width:46px;background:var(--forest)}

  /* Envelopes */
  .envelope{left:629px;width:457px;height:203px}
  .envelope--front{top:158px}
  .envelope--back{top:376px}
  .envelope__logo{position:absolute;left:21px;top:27px;color:var(--olive);font-size:20px}
  .envelope__accent{position:absolute;left:0;top:0;width:457px;height:203px}
  .envelope__flap{position:absolute;left:0;top:0;width:457px;height:56px}
  .envelope__flap-logo{position:absolute;left:0;width:100%;top:26px;text-align:center;color:var(--paper);font-size:13px}

  .contact-list{position:absolute;left:21px;top:133px;display:flex;flex-direction:column;gap:7px;font-size:5.6px;line-height:6.6px;color:var(--olive)}
  .contact-list .contact{display:flex;align-items:center;gap:6px}
  .contact-list svg{width:7px;height:7px;flex:none}

  /* Business cards */
  .card{top:614px;width:222px;height:127px}
  .card--front{left:629px}
  .card--back{left:865px;background:var(--forest)}
  .card__panel{position:absolute;left:0;top:0;width:94px;height:127px;background:var(--olive);display:flex;align-items:center;justify-content:center}
  .card__panel .wordmark{color:var(--paper);font-size:15px;margin-top:14px}
  .card__name{position:absolute;left:112px;top:18px;font-family:"Tinos",serif;font-size:11px;color:var(--olive);letter-spacing:.02em}
  .card__role{position:absolute;left:112px;top:32px;font-size:6px;color:var(--muted)}
  .card__divider{position:absolute;left:112px;top:42px;width:12px;height:1px;background:var(--olive)}
  .card .contact-list{left:112px;top:51px;gap:8px;font-size:5px;line-height:6px}
  .card__brand{position:absolute;left:0;width:100%;top:50px;text-align:center;color:var(--olive);font-size:17px}
  .card__tagline{position:absolute;left:0;width:100%;top:75px;text-align:center;color:var(--olive);font-size:7px;letter-spacing:.02em}
</style>
</head>
<body>

<svg width="0" height="0" style="position:absolute" aria-hidden="true">
  <defs>
    <symbol id="icon-phone" viewBox="0 0 24 24"><path fill="currentColor" d="M6.6 10.8c1.4 2.8 3.8 5.1 6.6 6.6l2.2-2.2c.3-.3.7-.4 1-.2 1.1.4 2.3.6 3.6.6.6 0 1 .4 1 1V20c0 .6-.4 1-1 1C10.6 21 3 13.4 3 4c0-.6.4-1 1-1h3.5c.6 0 1 .4 1 1 0 1.3.2 2.5.6 3.6.1.3 0 .7-.2 1l-2.3 2.2z"/></symbol>
    <symbol id="icon-globe" viewBox="0 0 24 24"><g fill="none" stroke="currentColor" stroke-width="2"><circle cx="12" cy="12" r="9"/><ellipse cx="12" cy="12" rx="4" ry="9"/><path d="M3 12h18M5 7h14M5 17h14"/></g></symbol>
    <symbol id="icon-pin" viewBox="0 0 24 24"><path fill="currentColor" d="M12 2a7 7 0 0 0-7 7c0 5.2 7 13 7 13s7-7.8 7-13a7 7 0 0 0-7-7zm0 9.5A2.5 2.5 0 1 1 12 6.5a2.5 2.5 0 0 1 0 5z"/></symbol>
  </defs>
</svg>

<!-- Letterhead -->
<section class="sheet letterhead">
  <div class="letterhead__logo-box"><span class="wordmark">Gombrevo</span></div>
  <h1 class="letterhead__company">Australia Gombrevo Pty Ltd.</h1>
  <div class="letterhead__rule letterhead__rule--top"></div>

  <div class="letter">
    <p class="letter__greeting">Dear Peter,</p>
    <p class="letter__para">Dolor sit amet, consectetuer adipiscing elit, sed diam nonummy nibh euismod tincidunt ut laoreet dolore magna aliquam erat volutpat. Ut wisi enim ad minim veniam, quis nostrud exerci tation ullamcorper suscipit lobortis nisl ut aliquip ex ea commodo consequat. Duis autem vel eum iriure dolor in hendrerit in vulputate velit esse molestie consequat, vel illum dolore eu feugiat nulla facilisis at vero eros et accumsan et iusto odio dignissim qui blandit praesent luptatum zzril delenit augue duis dolore te feugait nulla facilisi.</p>
    <p class="letter__para">Sit amet, cons ectetuer adipiscing elit, sed diam nonummy nibh euismod tincidunt ut laoreet dolore magna aliquam erat volutpat. Ut wisi enim ad minim veniam, quis nostrud exerci tation ullamcorper suscipit lobortis nisl ut aliquip ex ea commodo consequat.<br><span style="display:inline-block;text-indent:0;margin-left:-30px">Lorem ipsum dolor sit amet, consectetuer adipiscing elit, sed diam nonummy nibh euismod.</span></p>
    <p class="letter__para">Consectetuer adipiscing elit, sed diam nonummy nibh euismod tincidunt ut laoreet dolore magna aliquam erat volutpat. Ut wisi enim ad minim veniam, quis nostrud exerci tation ullamcorper suscipit lobortis nisl ut aliquip ex ea commodo consequat. Duis autem vel eum iriure dolor in hendrerit in vulputate velit esse molestie consequat, vel illum dolore eu feugiat nulla facilisis at vero eros et accumsan et iusto odio dignissim qui blandit praesent luptatum zzril delenit augue duis dolore te feugait nulla facilisi.</p>
    <p class="letter__para">Dipiscing elit, sed diam nonummy nibh euismod tincidunt ut laoreet dolore magna aliquam erat volutpat. Ut wisi enim ad minim veniam, quis nostrud exerci tation ullamcorper suscipit lobortis nisl ut aliquip ex ea commodo consequat.<br><span style="display:inline-block;text-indent:0;margin-left:-30px">Lorem ipsum dolor sit amet, consectetuer adipiscing elit, sed diam nonummy nibh euismod.</span></p>
  </div>

  <div class="letter__signature" role="img" aria-label="Handwritten signature of the sender"></div>
  <p class="letter__closing">Regards<br>Tom Hale</p>

  <div class="letterhead__rule letterhead__rule--bottom"></div>
  <div class="letterhead__footer">
    <div class="contact contact--phone"><svg><use href="#icon-phone"/></svg><span>1800 555 014</span></div>
    <div class="contact contact--web"><svg><use href="#icon-globe"/></svg><span>mara@gombrevo.com.au<br>www.gombrevo.com.au</span></div>
    <div class="contact contact--address"><svg><use href="#icon-pin"/></svg><span>4/22 Fenwick Road<br>Glen Arden Vic 3150</span></div>
  </div>
  <div class="letterhead__bar letterhead__bar--olive"></div>
  <div class="letterhead__bar letterhead__bar--forest"></div>
</section>

<!-- Envelope front -->
<section class="sheet envelope envelope--front">
  <svg class="envelope__accent" viewBox="0 0 457 203" aria-hidden="true">
    <polygon points="362,0 457,0 457,203 456,203 423,136" fill="var(--olive)"/>
    <polygon points="355,0 362,0 425,137 420,140" fill="var(--forest)"/>
    <polygon points="421,137 456,203 361,203" fill="var(--forest)"/>
    <polygon points="420,139 361,203 350,203" fill="var(--olive)"/>
  </svg>
  <span class="wordmark envelope__logo">Gombrevo</span>
  <div class="contact-list">
    <div class="contact"><svg><use href="#icon-phone"/></svg><span>1800 555 014</span></div>
    <div class="contact"><svg><use href="#icon-globe"/></svg><span>mara@gombrevo.com.au<br>www.gombrevo.com.au</span></div>
    <div class="contact"><svg><use href="#icon-pin"/></svg><span>4/22 Fenwick Road<br>Glen Arden Vic 3150</span></div>
  </div>
</section>

<!-- Envelope back -->
<section class="sheet envelope envelope--back">
  <svg class="envelope__flap" viewBox="0 0 457 56" aria-hidden="true">
    <path d="M0,0 H457 L440,42 Q434,55 420,55 H37 Q23,55 17,42 Z" fill="var(--olive)"/>
  </svg>
  <span class="wordmark envelope__flap-logo">Gombrevo</span>
  <div class="contact-list">
    <div class="contact"><svg><use href="#icon-phone"/></svg><span>1800 555 014</span></div>
    <div class="contact"><svg><use href="#icon-globe"/></svg><span>mara@gombrevo.com.au<br>www.gombrevo.com.au</span></div>
    <div class="contact"><svg><use href="#icon-pin"/></svg><span>4/22 Fenwick Road<br>Glen Arden Vic 3150</span></div>
  </div>
</section>

<!-- Business card front -->
<section class="sheet card card--front">
  <div class="card__panel"><span class="wordmark">Gombrevo</span></div>
  <p class="card__name">Mara Linde</p>
  <p class="card__role">Managing Director</p>
  <div class="card__divider"></div>
  <div class="contact-list">
    <div class="contact"><svg><use href="#icon-phone"/></svg><span>+ 61 (0) 400 555 318<br>1800 555 014</span></div>
    <div class="contact"><svg><use href="#icon-globe"/></svg><span>mara@gombrevo.com.au<br>www.gombrevo.com.au</span></div>
    <div class="contact"><svg><use href="#icon-pin"/></svg><span>4/22 Fenwick Road<br>Glen Arden Vic 3150</span></div>
  </div>
</section>

<!-- Business card back -->
<section class="sheet card card--back">
  <span class="wordmark card__brand">Gombrevo</span>
  <p class="card__tagline">Your furry friend deserves the best</p>
</section>

</body>
</html>
```